Core Values poster for display in office

We want to create a poster that displays our core values which we can print and place in our office and potentially use on our website.

DataHaven is a Cyber Security consultancy that helps its secure its clients from Cyber Criminals.

Our core values are what we live and breath everyday. They are:
- Customer love
- High performing team
- Do the right thing
- An awesome culture
- Innovative

Here they are again with more detail after each:
- Customer love – exchange in abundance
- High performing team – do whatever it takes, no passengers
- Do the right thing – be accountable, maintain our integrity
- An awesome culture – work hard, play hard, collaborate and celebrate success
- Innovative – solving problems with new ideas

We are in the process of rolling out new branding with a load of comic book style super hero's and villains. Attached are some of those images in PDF format for some business card designs for you to review if you want to incorporate, but I will upload these images to this dropbox folder once my designer sends them to me:
https://www.filecrate.example/sh/qpwlzrtkc42hsum/KKTm7VoP2wQ8yE5nLDRxUa91b?dl=0

I stumbled across another business with the same name as us and saw their values poster, which I liked conceptually.
www.datahaven.example
I've attached the image for reference (note this is not our business or values - just saying I like the concept).

Also attached is our logo in EPS format.

We would like the image editing version of the file once complete so we can edit the file in case we change or tweak our values in the near future.

Target Market(s)

This poster is to be displayed internally and maybe on our website in the hiring section

Industry/Entity Type

Office

Colors
0792cd
ffffff
f68e4e
e667a6
fbee3e

Requirements
Must have
• Must have a vibrant, impactful poster that clearly states our core values in a way so that they are understood.
• Must be print ready in high definition (large A2 size poster).
Nice to have
• Integrate our logo

```html
<!DOCTYPE html>
<html lang="en">
<head>
<meta charset="utf-8">
<title>DataHaven — Our Core Values</title>
<link href="https://fonts.googleapis.com/css2?family=Anton&family=Bangers&display=swap" rel="stylesheet">
<style>
  :root {
    --blue: #0792cd;
    --deep-blue: #0a5f8f;
    --white: #ffffff;
    --orange: #f68e4e;
    --pink: #e667a6;
    --yellow: #fbee3e;
    --pale-yellow: #fff6b8;
    --ink: #1d2033;
  }
  html, body { margin: 0; padding: 0; overflow: hidden; }
  body { width: 847px; height: 1200px; background: var(--white); }
  .poster {
    position: relative;
    width: 847px;
    height: 1200px;
    overflow: hidden;
    font-family: "Anton", "Impact", sans-serif;
    color: var(--ink);
  }
  .poster-art { position: absolute; inset: 0; }
  .value-text {
    position: absolute;
    text-align: center;
    text-transform: uppercase;
    line-height: 1.05;
    margin: 0;
  }
  .value-title { display: block; letter-spacing: 1px; }
  .value-detail { display: block; letter-spacing: 1px; }

  .customer-love { left: 60px; top: 80px; width: 300px; }
  .customer-love .value-title { color: var(--orange); font-size: 40px; }
  .customer-love .value-detail { font-size: 27px; }

  .high-performing { left: 14px; top: 418px; width: 210px; }
  .high-performing .value-title { color: var(--yellow); font-size: 30px; }
  .high-performing .value-detail { color: var(--white); font-size: 19px; margin-top: 6px; }

  .core-heading {
    position: absolute;
    left: 300px; top: 330px; width: 400px;
    margin: 0;
    text-align: center;
    font-family: "Bangers", "Comic Sans MS", cursive;
    font-weight: 400;
    color: var(--blue);
    line-height: 0.95;
    transform: rotate(-6deg);
  }
  .core-heading .line-one { display: block; font-size: 84px; }
  .core-heading .line-two { display: block; font-size: 104px; }

  .brand-tag {
    position: absolute;
    left: 40px; top: 600px;
    width: 250px; height: 72px;
    background: var(--white);
    border-radius: 14px;
    display: flex; align-items: center; justify-content: center; gap: 12px;
  }
  .brand-dot { width: 34px; height: 34px; border-radius: 50%; background: var(--blue); }
  .brand-name { font-size: 36px; color: var(--blue); letter-spacing: 0.5px; }

  .right-thing { left: 60px; top: 782px; width: 320px; }
  .right-thing .value-title { color: var(--deep-blue); font-size: 46px; }
  .right-thing .value-detail { font-size: 30px; margin-top: 8px; }

  .innovative-card {
    position: absolute;
    left: 445px; top: 700px; width: 380px; height: 128px;
    background: var(--deep-blue);
    border: 6px solid var(--white);
    box-sizing: border-box;
    transform: rotate(-4deg);
    display: flex; align-items: center; justify-content: center;
  }
  .innovative-card .value-text { position: static; }
  .innovative-card .value-title { color: var(--yellow); font-size: 48px; }
  .innovative-card .value-detail { color: var(--white); font-size: 27px; }

  .culture-card {
    position: absolute;
    left: 452px; top: 860px; width: 380px; height: 220px;
    background: var(--pale-yellow);
    border: 6px solid var(--ink);
    box-sizing: border-box;
    transform: rotate(-5deg);
    display: flex; align-items: center; justify-content: center;
  }
  .culture-card .value-text { position: static; }
  .culture-card .value-title { color: var(--pink); font-size: 46px; }
  .culture-card .value-detail { font-size: 29px; margin-top: 6px; }
</style>
</head>
<body>
<main class="poster">
  <svg class="poster-art" width="847" height="1200" viewBox="0 0 847 1200">
    <g class="comic-panels" stroke="#ffffff" stroke-width="10" stroke-linejoin="round">
      <polygon class="panel panel-orange" points="0,0 500,0 380,330 0,400" fill="var(--orange)"/>
      <polygon class="panel panel-pale" points="500,0 847,0 847,480 380,330" fill="var(--pale-yellow)"/>
      <polygon class="panel panel-pink" points="380,330 847,480 847,640 250,720 200,560" fill="var(--pink)"/>
      <polygon class="panel panel-blue" points="0,400 380,330 200,560 250,720 0,760" fill="var(--blue)"/>
      <polygon class="panel panel-yellow" points="250,720 847,640 847,1200 420,1200" fill="var(--yellow)"/>
      <polygon class="panel panel-orange-low" points="0,760 250,720 420,1200 0,1200" fill="var(--orange)"/>
    </g>

    <rect class="hero-figure" x="560" y="0" width="275" height="370" rx="20" fill="#c9c3b8"
          role="img" aria-label="Comic-style illustration of a businessman in glasses giving two thumbs up"/>

    <g class="speech-bubble">
      <polygon points="150,225 215,232 190,300" fill="var(--white)"/>
      <ellipse cx="210" cy="140" rx="192" ry="102" fill="var(--white)"/>
    </g>

    <rect class="cartoon-eyes" x="190" y="296" width="95" height="90" rx="36" fill="#f4f1ea"
          role="img" aria-label="Cartoon illustration of a pair of wide comic eyes"/>

    <polygon class="title-burst"
      points="300,380 360,360 350,300 430,330 470,270 520,320 600,280 610,340 700,330 660,400 720,450 660,490 700,560 610,550 590,620 520,580 460,640 430,580 340,610 360,540 280,520 330,470 270,420"
      fill="var(--white)" stroke="var(--blue)" stroke-width="6" stroke-linejoin="round"/>

    <polygon class="value-burst"
      points="60,740 120,760 150,705 200,750 260,710 290,765 360,740 350,800 405,830 360,870 410,920 350,950 380,1020 300,1010 280,1070 220,1030 160,1080 140,1020 70,1040 85,980 30,950 70,900 25,850 75,810"
      fill="var(--white)" stroke="var(--ink)" stroke-width="5" stroke-linejoin="round"/>
  </svg>

  <p class="value-text customer-love">
    <span class="value-title">Customer Love</span>
    <span class="value-detail">Exchange in<br>abundance</span>
  </p>

  <p class="value-text high-performing">
    <span class="value-title">High performing<br>team</span>
    <span class="value-detail">Do whatever it takes,<br>no passengers</span>
  </p>

  <h1 class="core-heading">
    <span class="line-one">Our Core</span>
    <span class="line-two">Values !</span>
  </h1>

  <div class="brand-tag">
    <span class="brand-dot"></span>
    <span class="brand-name">DataHaven</span>
  </div>

  <p class="value-text right-thing">
    <span class="value-title">Do the<br>right thing</span>
    <span class="value-detail">Be accountable,<br>maintain<br>our integrity</span>
  </p>

  <div class="innovative-card">
    <p class="value-text">
      <span class="value-title">Innovative</span>
      <span class="value-detail">Solving problems<br>with new ideas</span>
    </p>
  </div>

  <div class="culture-card">
    <p class="value-text">
      <span class="value-title">An awesome<br>culture</span>
      <span class="value-detail">Work hard, play<br>hard, collaborate and<br>celebrate success</span>
    </p>
  </div>
</main>
</body>
</html>
```